TGV Electricial Contracting Services

Hi guys, after a design for my small electrical company, have logo design files to be incorporated into the layout, the basic concept is electrical contracting services for residential, commercial, industrial & data services, image is clean clear and strong,

Card format is to have a nice clean logo on front,with maybe the Residential – commercial – industrial - data, followed with licensed & insured, followed by contact details on backside of the card.

Target Market(s)

Residential, commercial, industrial sectors.

Industry/Entity Type

Electrical

Contact Information for Business Card

TGV logo,
Residential – commercial – industrial - data
REC: 57310
Email: tgv@wavolink.net.au
Phone: 0472 358 129

Requirements
Must have
• Clean & strong design.
Nice to have
• If possible, I would like the logo colours inverted so the text is orange and the background is black on the front of the card, then the backside of the card be the reverse colour
Should not have
• No Sparks, lightning bolts,

```html
<!DOCTYPE html>
<html lang="en">
<head>
<meta charset="utf-8">
<title>TGV Business Card</title>
<link href="https://fonts.googleapis.com/css2?family=Open+Sans:wght@400;600;700;800&display=swap" rel="stylesheet">
<style>
  :root {
    --orange: #f5832a;
    --black: #050505;
    --grey-text: #8a8a8a;
    --bg: #e9e9e9;
  }
  * { margin: 0; padding: 0; box-sizing: border-box; }
  html, body { width: 1200px; height: 1000px; overflow: hidden; }
  body {
    background: var(--bg);
    font-family: "Open Sans", Arial, sans-serif;
    position: relative;
  }
  .card {
    position: absolute;
    left: 250px;
    width: 700px;
    height: 400px;
    overflow: hidden;
  }
  .card--front { top: 80px; background: var(--black); }
  .card--back { top: 520px; background: var(--orange); }

  .brand__name {
    font-weight: 800; line-height: 1;
    letter-spacing: 2px; white-space: nowrap;
  }
  .brand__full { font-weight: 700; white-space: nowrap; }

  /* Front */
  .front__band {
    position: absolute; left: 0; right: 0; bottom: 0;
    height: 52px; background: var(--orange);
  }
  .front__rule {
    position: absolute; left: 282px; right: 0; top: 108px;
    height: 5px; background: var(--orange);
    box-shadow: 0 0 10px rgba(245,131,42,0.7);
  }
  .front__content {
    position: absolute; left: 120px; top: 50px;
    display: flex; flex-direction: column;
  }
  .front__brand .brand__name { font-size: 72px; color: var(--orange); }
  .front__brand .brand__full { font-size: 15px; color: var(--orange); margin-top: 4px; }
  .front__sectors {
    margin-top: 22px;
    font-size: 14px; color: var(--grey-text); letter-spacing: 0.5px;
  }
  .front__licence {
    margin-top: 6px;
    font-size: 14px; color: var(--grey-text); letter-spacing: 0.5px;
  }
  .front__contact {
    margin-top: 14px; margin-left: -16px;
    list-style: none; font-size: 14px; color: var(--grey-text);
    letter-spacing: 1px;
  }
  .front__contact li { display: flex; align-items: center; height: 24px; }
  .front__contact svg { width: 10px; height: 10px; margin-right: 6px; flex: none; }

  /* Back */
  .back__rule {
    position: absolute; left: 0; top: 138px; width: 424px;
    height: 6px; background: var(--black);
  }
  .back__brand { position: absolute; left: 432px; top: 128px; }
  .back__brand .brand__name { color: var(--black); font-size: 96px; }
  .back__brand .brand__full { color: var(--black); font-size: 18px; margin-top: 4px; }
</style>
</head>
<body>
  <section class="card card--front" aria-label="Business card front">
    <div class="front__rule"></div>
    <div class="front__content">
      <div class="front__brand">
        <div class="brand__name">TGV</div>
        <div class="brand__full">Tate Grayson Electrical</div>
      </div>
      <p class="front__sectors">Residential - Commercial - Industrial - Data</p>
      <p class="front__licence">Licensed &amp; Insured &nbsp;|&nbsp; REC: 57310</p>
      <ul class="front__contact">
        <li>
          <svg viewBox="0 0 10 10" aria-hidden="true"><polyline points="3,1 7,5 3,9" fill="none" stroke="#f5832a" stroke-width="1.6"/></svg>
          0472-358-129
        </li>
        <li>
          <svg viewBox="0 0 10 10" aria-hidden="true"><polyline points="3,1 7,5 3,9" fill="none" stroke="#f5832a" stroke-width="1.6"/></svg>
          tgv@wavolink.net.au
        </li>
      </ul>
    </div>
    <div class="front__band"></div>
  </section>

  <section class="card card--back" aria-label="Business card back">
    <div class="back__rule"></div>
    <div class="back__brand">
      <div class="brand__name">TGV</div>
      <div class="brand__full">Tate Grayson Electrical</div>
    </div>
  </section>
</body>
</html>
```